DL size flyer design for renovations and extensions construction company

We are looking for a flyer design for a construction company specialising in renovations, extensions, and minor building works. The aim is for anyone needing any home construction works to pick up the phone and call us. The flyers will be delivered primarily to letterboxes of homes. We want the flyers to stick out from all the other things people get in the mail by any means possible.

Target Market(s)

The audience we target is residential home owners and are looking to deliver these letters to home letterboxes.

Industry/Entity Type

Residential Construction

Font styles to use
Sans Serif

Colors
000000
ffffff

Requirements
Must have
• 1 - Places for 4 photos with descriptions reading: (1) Bathroom Renovations (4) Kitchen Renovations (3) Home Extensions (4) Outdoor works and landscaping. This may be on the reverse side of the DL flyer.
• 2 - Fonts to be used are (1) Brandon Grotesque (All caps) for main heading, (2) Montserrat SemiBold (All caps) for Headings, (3) Lato for text.
• 3 - Copy of the finished document in PDF and indesign formats.
• 4 - Placeholders for copy (look at the pelvaridge.com website for now)
Nice to have
• A modern looking design.
Should not have
• Not all photos attached are necessarily required. Up to you to use your creativity to decide on the best combination.

```html
<!DOCTYPE html>
<html lang="en">
<head>
<meta charset="utf-8">
<title>PelvaRidge – Trifold Flyer</title>
<link rel="stylesheet" href="https://fonts.googleapis.com/css2?family=Montserrat:wght@300;600;700&family=Lato:wght@300;400&display=swap">
<style>
  :root {
    --ink: #1d1a1b;
    --paper: #ffffff;
    --backdrop: #7b7b7b;
    --accent: #1f9a62;
    --accent-soft: #4fb98a;
    --body-text: #3a3a3a;
    --muted: #8a8a8a;
  }
  * { box-sizing: border-box; margin: 0; padding: 0; }
  html, body { width: 1200px; height: 1200px; overflow: hidden; background: var(--backdrop); }
  .brochure {
    position: absolute; left: 60px; top: 218px;
    width: 1080px; height: 764px;
    background: var(--paper);
    display: flex;
    box-shadow: 0 10px 30px rgba(0,0,0,.25);
  }
  .panel { position: relative; width: 360px; height: 100%; overflow: hidden; }
  .panel + .panel { border-left: 1px solid #e6e6e6; }

  /* Left panel */
  .garden-photo {
    position: absolute; left: 0; top: 0; width: 100%; height: 250px;
    background: linear-gradient(160deg, #9cc35a 0%, #5e8f3a 40%, #7a3c26 70%, #cfc6b8 100%);
  }
  .service-icon { position: absolute; left: 125px; top: 290px; width: 110px; height: 110px; }
  .service-title {
    position: absolute; left: 40px; top: 430px; width: 280px;
    font-family: 'Montserrat', sans-serif; font-weight: 600; font-size: 15px;
    line-height: 1.25; letter-spacing: .5px; text-transform: uppercase; color: var(--accent);
  }
  .service-copy {
    position: absolute; left: 40px; top: 480px; width: 280px;
    font-family: 'Lato', sans-serif; font-weight: 300; font-size: 14px;
    line-height: 1.45; color: var(--body-text);
  }
  .service-copy p + p { margin-top: 12px; }

  /* Middle & right panels */
  .brand {
    position: absolute; left: 0; width: 100%; text-align: center;
  }
  .brand-name {
    font-family: 'Montserrat', sans-serif; font-weight: 700; font-size: 34px;
    letter-spacing: 1px; color: var(--ink); text-transform: uppercase;
  }
  .brand-tagline {
    margin-top: 4px;
    font-family: 'Lato', sans-serif; font-weight: 300; font-size: 13px;
    letter-spacing: 3px; color: var(--ink); text-transform: uppercase;
  }
  .brand-top { top: 52px; }
  .brand-bottom { top: 662px; }
  .ink-band { position: absolute; left: 0; top: 150px; width: 100%; height: 40px; background: var(--ink); }
  .quote-block {
    position: absolute; left: 0; top: 580px; width: 100%; height: 184px;
    background: var(--ink); text-align: center; padding-top: 56px;
    font-family: 'Montserrat', sans-serif; font-weight: 300; text-transform: uppercase;
  }
  .quote-label { color: var(--accent); font-size: 15px; letter-spacing: 1px; }
  .quote-line { color: var(--muted); font-size: 15px; letter-spacing: .5px; margin-top: 2px; }

  .family-photo { position: absolute; left: 360px; top: 0; width: 720px; height: 764px; pointer-events: none; }

  .slogan {
    position: absolute; left: 30px; top: 70px; width: 300px; text-align: center;
  }
  .slogan-kicker {
    font-family: 'Lato', sans-serif; font-size: 13px; letter-spacing: 2.5px;
    text-transform: uppercase; color: var(--ink);
  }
  .slogan-heading {
    margin-top: 14px; padding: 12px 0;
    border-top: 1px solid var(--accent-soft); border-bottom: 1px solid var(--accent-soft);
    font-family: 'Montserrat', sans-serif; font-weight: 300; font-size: 20px;
    line-height: 1.3; letter-spacing: 1px; text-transform: uppercase; color: var(--accent-soft);
  }
</style>
</head>
<body>
<div class="brochure">
  <section class="panel panel-service">
    <div class="garden-photo" role="img" aria-label="Photo of a landscaped garden with timber decking, planter box and lawn"></div>
    <svg class="service-icon" viewBox="0 0 110 110" aria-hidden="true">
      <circle cx="55" cy="55" r="52" fill="none" stroke="#1d1a1b" stroke-width="1.5"/>
      <path d="M35 58 C25 55 26 40 38 40 C38 28 56 26 60 36 C72 32 82 44 74 54 C78 64 66 70 58 64 L58 88 L50 88 L50 64 C44 68 36 66 35 58 Z" fill="none" stroke="#1d1a1b" stroke-width="1.5"/>
    </svg>
    <h2 class="service-title">Outdoor works<br>and landscaping</h2>
    <div class="service-copy">
      <p>Home living spans across both internal and external environments and a complete home needs to consider integration into the surrounding land.</p>
      <p>Whether it be landscaping works, swimming pools or outdoor buildings – PelvaRidge can deliver all project designs both large scale and compact.</p>
    </div>
  </section>

  <section class="panel panel-contact">
    <div class="brand brand-top">
      <div class="brand-name">Pelva Ridge</div>
      <div class="brand-tagline">Committed to excellence</div>
    </div>
    <div class="ink-band"></div>
    <div class="quote-block">
      <div class="quote-label">Request a quote</div>
      <div class="quote-line">0400 715 228</div>
      <div class="quote-line">info@pelvaridge.com</div>
    </div>
  </section>

  <section class="panel panel-cover">
    <div class="slogan">
      <div class="slogan-kicker">Build. Renovate. Extend.</div>
      <h1 class="slogan-heading">Looking to make your home bigger or better?</h1>
    </div>
    <div class="brand brand-bottom">
      <div class="brand-name">Pelva Ridge</div>
      <div class="brand-tagline">Committed to excellence</div>
    </div>
  </section>

  <svg class="family-photo" viewBox="0 0 720 764" role="img" aria-label="Photo of a smiling family lying together on a rug in a bright white living room">
    <defs>
      <linearGradient id="livingRoom" x1="0" y1="0" x2="0" y2="1">
        <stop offset="0" stop-color="#f3eee6"/>
        <stop offset=".45" stop-color="#e9e2d6"/>
        <stop offset=".7" stop-color="#8fb3c4"/>
        <stop offset="1" stop-color="#d9d1c4"/>
      </linearGradient>
    </defs>
    <polygon points="0,190 360,190 360,260 720,260 720,620 360,620 360,580 0,580" fill="url(#livingRoom)"/>
  </svg>
</div>
</body>
</html>
```